Lotus Reed Cuisine Road Billboard

Road Billboard I need all of this information on it
Authentic Thai Food Bangkok Style
6.5 Miles on the right
4318 Maple Hollow Rd Otto NC
828-555-0147

```html
<!DOCTYPE html>
<html lang="en">
<head>
<meta charset="UTF-8">
<title>Lotus Reed Cuisine – Road Billboard</title>
<link rel="stylesheet" href="https://fonts.googleapis.com/css2?family=Exo+2:wght@600&family=Open+Sans:wght@500;600&display=swap">
<style>
  :root {
    --page-bg: #e9ecef;
    --board-bg: #1d1b1c;
    --gold: #d2a53a;
    --white: #f4f1ec;
    --flame: #c8621c;
    --ember: #4a2a14;
  }
  * { margin: 0; padding: 0; box-sizing: border-box; }
  html, body {
    width: 1200px;
    height: 900px;
    overflow: hidden;
    background: var(--page-bg);
  }
  .billboard {
    position: absolute;
    left: 40px;
    top: 280px;
    width: 1120px;
    height: 340px;
    background: var(--board-bg);
    overflow: hidden;
    font-family: "Open Sans", sans-serif;
  }
  .dish-photo {
    position: absolute;
    left: 520px;
    top: 0;
    width: 500px;
    height: 240px;
    background:
      radial-gradient(ellipse 40% 55% at 28% 60%, var(--flame) 0%, rgba(200,98,28,0.35) 45%, transparent 75%),
      radial-gradient(ellipse 55% 45% at 62% 55%, #6b6a66 0%, #3b3937 45%, transparent 80%),
      radial-gradient(ellipse 60% 60% at 50% 50%, var(--ember) 0%, transparent 80%);
  }
  .headline {
    position: absolute;
    left: 34px;
    top: 88px;
    font-family: "Exo 2", sans-serif;
    font-weight: 600;
    font-size: 44px;
    line-height: 1.12;
    color: var(--white);
    letter-spacing: 0.5px;
  }
  .headline .accent { color: var(--gold); }
  .direction-banner {
    position: absolute;
    right: 24px;
    top: 32px;
    width: 360px;
    height: 52px;
  }
  .direction-banner svg { position: absolute; inset: 0; }
  .direction-banner span {
    position: relative;
    display: block;
    padding-left: 18px;
    line-height: 52px;
    font-weight: 600;
    font-size: 25px;
    color: var(--board-bg);
    white-space: nowrap;
  }
  .brand {
    position: absolute;
    left: 34px;
    bottom: 34px;
    display: flex;
    align-items: center;
    gap: 10px;
    font-family: "Exo 2", sans-serif;
    font-weight: 600;
    font-size: 22px;
    color: var(--gold);
    white-space: nowrap;
  }
  .brand .dot {
    width: 14px;
    height: 14px;
    border-radius: 50%;
    background: var(--gold);
  }
  .contact {
    position: absolute;
    bottom: 30px;
    display: flex;
    align-items: center;
    gap: 12px;
    font-weight: 500;
    font-size: 32px;
    line-height: 1.2;
    color: var(--gold);
    white-space: nowrap;
  }
  .contact svg { width: 26px; height: 26px; flex: none; }
  .contact.phone { left: 270px; letter-spacing: 1px; }
  .contact.address { left: 560px; }
</style>
</head>
<body>
  <main class="billboard">
    <div class="dish-photo" role="img" aria-label="Stir-fried shrimp and vegetables tossed in a flaming wok"></div>

    <h1 class="headline">Authentic <span class="accent">thai food</span><br>Bangkok style</h1>

    <div class="direction-banner">
      <svg viewBox="0 0 360 52" preserveAspectRatio="none" aria-hidden="true">
        <polygon points="0,0 330,0 360,26 330,52 0,52" fill="var(--gold)"/>
      </svg>
      <span>6.5 Miles on the right</span>
    </div>

    <div class="brand"><span class="dot"></span>Lotus Reed Cuisine</div>

    <div class="contact phone">
      <svg viewBox="0 0 24 24" aria-hidden="true">
        <circle cx="12" cy="12" r="10.5" fill="none" stroke="var(--white)" stroke-width="1.4"/>
        <path d="M8.6 7.2l1.8-.4 1 2.3-1.2.9a6.5 6.5 0 0 0 3 3l.9-1.2 2.3 1-.4 1.8c-3.8.4-7.8-3.6-7.4-7.4z" fill="none" stroke="var(--white)" stroke-width="1.2" stroke-linejoin="round"/>
      </svg>
      828-555-0147
    </div>

    <div class="contact address">
      <svg viewBox="0 0 24 24" aria-hidden="true">
        <circle cx="12" cy="12" r="10.5" fill="none" stroke="var(--white)" stroke-width="1.4"/>
        <path d="M12 18.5s-4.2-4.4-4.2-7.6a4.2 4.2 0 0 1 8.4 0c0 3.2-4.2 7.6-4.2 7.6z" fill="none" stroke="var(--white)" stroke-width="1.2"/>
        <circle cx="12" cy="10.8" r="1.5" fill="none" stroke="var(--white)" stroke-width="1.2"/>
      </svg>
      4318 Maple Hollow Rd Otto NC
    </div>
  </main>
</body>
</html>
```